I need to redesign this website. Modern Fun Professional Redesign For www.JollyPerkHub.com = New Name www.ClaimVouchly.com

Use existing content as it is on website exactly and we will revise after initial mock ups.

The new name will be ClaimVouchly.com please make a quick logo for this site too while redesigning.

Make it look like an official website....

Target Market(s)

Consumers that are redeeming certificates that businesses gave to them as a gift for customer loyalty,e tc.

Industry/Entity Type

It Professional

Logo Text

www.ClaimVouchly.com

Number of Pages Required

4 page

Colors

Designer to choose colors to be used in the design.

Requirements
Must have
• Must look professional, build trust and credibility.
Nice to have
• open
Should not have
• open

```html
<!DOCTYPE html>
<html lang="en">
<head>
<meta charset="utf-8">
<title>Claim Vouchly</title>
<link href="https://fonts.googleapis.com/css2?family=Dancing+Script:wght@700&family=Open+Sans:wght@400;600;700;800&display=swap" rel="stylesheet">
<style>
:root{
  --orange:#e2692a;
  --green:#7dc24b;
  --teal:#1f6c85;
  --ink:#222;
  --grey:#666;
  --dark:#1c1c1c;
  --gold:#d4a537;
  --quote:#dcdcdc;
  --white:#fff;
}
html,body{margin:0;padding:0;overflow:hidden;}
body{width:1200px;height:2493px;background:var(--white);font-family:"Open Sans",Arial,sans-serif;color:var(--ink);}
.page{position:relative;width:1200px;height:2493px;overflow:hidden;}
.abs{position:absolute;}
.script{font-family:"Dancing Script",cursive;font-weight:700;}

/* header */
.brand{display:flex;align-items:center;gap:12px;}
.brand-mark{width:52px;height:52px;border-radius:50%;background:var(--green);}
.brand-name{font-family:"Open Sans",Arial,sans-serif;font-weight:600;font-size:28px;color:var(--orange);}
.site-header .brand{left:100px;top:36px;}
.main-nav{top:41px;left:0;width:1200px;}
.main-nav a{position:absolute;font-size:15px;font-weight:600;color:var(--ink);text-decoration:none;letter-spacing:.3px;white-space:nowrap;}

/* hero */
.hero{left:0;top:88px;}
.hero-title{top:212px;left:0;width:1200px;text-align:center;color:var(--white);font-size:56px;line-height:68px;text-shadow:0 2px 6px rgba(0,0,0,.35);}
.slide-arrow{top:386px;width:38px;height:38px;border-radius:50%;}
.slide-arrow.prev{left:26px;}
.slide-arrow.next{left:1136px;background:rgba(0,0,0,.35);}

/* welcome */
.welcome-title{top:806px;left:0;width:1200px;text-align:center;color:var(--orange);font-size:32px;}
.welcome-text{top:882px;left:300px;width:600px;text-align:center;font-size:12.5px;line-height:24px;color:var(--grey);margin:0;}
.cert-search{top:1002px;left:429px;width:341px;height:50px;display:flex;}
.cert-search .field{flex:1;border:1px solid #cfcfcf;border-right:none;font-size:13px;color:#888;padding-left:12px;display:flex;align-items:center;box-sizing:border-box;}
.cert-search .go{width:74px;background:var(--green);color:var(--white);font-weight:700;font-size:22px;display:flex;align-items:center;justify-content:center;}

/* info form */
.info{top:1153px;left:0;width:1200px;height:516px;background:
  radial-gradient(ellipse 700px 260px at 30% 20%,rgba(74,132,96,.55),transparent 70%),
  radial-gradient(ellipse 600px 240px at 85% 30%,rgba(58,112,120,.6),transparent 70%),
  linearGradient;background:linear-gradient(180deg,#2f6f6c 0%,#26697c 40%,#1f6c85 70%,#2b94a8 100%);}
.info-title{top:1216px;left:0;width:1200px;text-align:center;color:var(--white);font-size:32px;}
.input-box{border:2px solid var(--white);box-sizing:border-box;color:var(--white);font-size:12px;font-weight:600;padding:9px 12px;}
.submit-btn{top:1551px;left:527px;width:136px;height:48px;background:var(--green);border:1px solid #b9e39a;border-radius:4px;box-sizing:border-box;color:var(--white);font-weight:700;font-size:18px;letter-spacing:.5px;display:flex;align-items:center;justify-content:center;}

/* testimonial */
.customer-photo{top:1768px;left:103px;width:304px;height:196px;border-radius:50%;border:3px solid var(--gold);box-sizing:border-box;background:
  radial-gradient(ellipse 90px 70px at 70% 35%,rgba(240,226,210,.85),transparent 70%),
  radial-gradient(ellipse 80px 70px at 35% 45%,rgba(225,190,160,.8),transparent 70%),
  radial-gradient(ellipse 120px 60px at 30% 95%,rgba(240,150,40,.9),transparent 70%),
  linear-gradient(135deg,#6e6a66 0%,#9c8f84 40%,#c9b9a6 65%,#7b8a96 100%);}
.quote-mark{top:1752px;left:434px;font-size:140px;line-height:1;color:var(--quote);font-family:"Open Sans",Arial,sans-serif;font-weight:800;}
.testimonial-title{top:1782px;left:532px;color:var(--orange);font-size:27px;}
.testimonial-text{top:1838px;left:532px;width:520px;font-size:13px;line-height:32px;color:#444;margin:0;}
.testimonial-author{top:1917px;left:532px;font-size:15px;font-weight:600;color:var(--ink);}
.testimonial-author span{font-weight:400;font-size:13px;}
.round-btn{width:26px;height:26px;border-radius:50%;border:1.5px solid #777;box-sizing:border-box;}

/* footer */
.site-footer{top:2040px;left:0;}
.footer-brand{top:2130px;left:0;width:1200px;display:flex;justify-content:center;}
.footer-nav{top:2257px;left:0;width:1200px;text-align:center;color:var(--white);font-size:13px;font-weight:600;}
.footer-nav a{color:var(--white);text-decoration:none;}
.footer-nav .sep{margin:0 14px;}
.social{top:2320px;width:44px;height:44px;border-radius:50%;border:2px solid var(--white);box-sizing:border-box;display:flex;align-items:center;justify-content:center;}
.social::after{content:"";width:14px;height:14px;border-radius:50%;background:var(--white);}
.footer-rule{top:2410px;left:96px;width:1006px;border-top:1px dashed #888;}
.copyright{top:2444px;left:0;width:1200px;text-align:center;color:var(--white);font-size:12px;}
</style>
</head>
<body>
<div class="page">

  <header class="site-header">
    <div class="abs brand"><span class="brand-mark"></span><span class="brand-name">Claim Vouchly</span></div>
    <nav class="abs main-nav">
      <a style="left:643px">HOME</a>
      <a style="left:741px">CONTACT US</a>
      <a style="left:889px">TESTIMONIALS</a>
      <a style="left:1050px">TERMS</a>
    </nav>
  </header>

  <section class="hero-section">
    <svg class="abs hero" width="1200" height="635" viewBox="0 0 1200 635">
      <defs>
        <linearGradient id="heroFill" x1="0" y1="0" x2="0" y2="1">
          <stop offset="0" stop-color="#2f6a2c"/>
          <stop offset=".25" stop-color="#4a7d3a"/>
          <stop offset=".45" stop-color="#6f8a5a"/>
          <stop offset=".55" stop-color="#2fb3c0"/>
          <stop offset=".8" stop-color="#169bb0"/>
          <stop offset="1" stop-color="#0e7a92"/>
        </linearGradient>
        <radialGradient id="heroCliff" cx=".82" cy=".3" r=".28">
          <stop offset="0" stop-color="#b7a78a" stop-opacity=".75"/>
          <stop offset="1" stop-color="#b7a78a" stop-opacity="0"/>
        </radialGradient>
        <radialGradient id="heroSky" cx=".72" cy=".05" r=".22">
          <stop offset="0" stop-color="#3f8fd6" stop-opacity=".8"/>
          <stop offset="1" stop-color="#3f8fd6" stop-opacity="0"/>
        </radialGradient>
        <radialGradient id="heroBoat" cx=".5" cy=".6" rx=".4" r=".35" gradientTransform="translate(0 .3) scale(1 .5)">
          <stop offset="0" stop-color="#8fe03a" stop-opacity=".55"/>
          <stop offset="1" stop-color="#8fe03a" stop-opacity="0"/>
        </radialGradient>
        <linearGradient id="heroEdge" x1="0" x2="1">
          <stop offset="0" stop-color="#7dc24b"/>
          <stop offset=".5" stop-color="#e2692a"/>
          <stop offset="1" stop-color="#2a8aa0"/>
        </linearGradient>
        <clipPath id="heroClip"><path d="M0 62 Q600 -60 1200 62 L1200 567 Q600 690 0 567 Z"/></clipPath>
      </defs>
      <g role="img" aria-label="Photo of two people paddling a green kayak on turquoise water beside a forested limestone cliff" clip-path="url(#heroClip)">
        <rect width="1200" height="635" fill="url(#heroFill)"/>
        <rect width="1200" height="635" fill="url(#heroCliff)"/>
        <rect width="1200" height="635" fill="url(#heroSky)"/>
        <rect width="1200" height="635" fill="url(#heroBoat)"/>
      </g>
      <path d="M0 62 Q600 -60 1200 62" fill="none" stroke="url(#heroEdge)" stroke-width="4"/>
      <path d="M0 567 Q600 690 1200 567" fill="none" stroke="url(#heroEdge)" stroke-width="4"/>
    </svg>
    <h1 class="abs hero-title script" style="margin:0">What good is it to receive a gift<br>certificate if you can't use it?</h1>
    <svg class="abs slide-arrow prev" viewBox="0 0 38 38"><path d="M22 12 L15 19 L22 26" fill="none" stroke="#fff" stroke-width="3"/></svg>
    <svg class="abs slide-arrow next" viewBox="0 0 38 38"><path d="M16 12 L23 19 L16 26" fill="none" stroke="#fff" stroke-width="3"/></svg>
  </section>

  <section class="welcome">
    <h2 class="abs welcome-title script" style="margin:0">Welcome To The Claim Vouchly</h2>
    <p class="abs welcome-text">Our goal is to make it easy for you to redeem your certificate and our philosophy is this: "What good is it to receive a gift certificate if you can't use it?".If you have any questions about how to redeem a certain certificate, please contact us. We are here to help</p>
    <div class="abs cert-search"><div class="field">Certificate Id</div><div class="go">Go!</div></div>
  </section>

  <section class="info-section">
    <div class="abs info" role="img" aria-label="Faded teal photo of a lagoon with travel doodles of paper planes, an envelope and a gift box"></div>
    <h2 class="abs info-title script" style="margin:0">Submit Your Information</h2>
    <div class="abs input-box" style="top:1303px;left:301px;width:287px;height:38px">Name:</div>
    <div class="abs input-box" style="top:1303px;left:612px;width:287px;height:38px">Phone.no:</div>
    <div class="abs input-box" style="top:1361px;left:301px;width:287px;height:38px">Certificate Id:</div>
    <div class="abs input-box" style="top:1361px;left:612px;width:287px;height:38px">Email:</div>
    <div class="abs input-box" style="top:1421px;left:301px;width:598px;height:85px">How May We Assist You?</div>
    <div class="abs submit-btn">SUBMIT</div>
  </section>

  <section class="testimonial">
    <div class="abs customer-photo" role="img" aria-label="Photo of a smiling couple taking a selfie in a city street"></div>
    <div class="abs quote-mark">&ldquo;</div>
    <h2 class="abs testimonial-title script" style="margin:0">What Our Customers Are Saying</h2>
    <p class="abs testimonial-text">" Marla was a "saving grace." She followed up and helped me book the vacation and<br>air fare. Marla was positive and did everything she promised to do. "</p>
    <div class="abs testimonial-author">JUNE P, <span>Creative Manager</span></div>
    <svg class="abs round-btn" style="top:1908px;left:1034px" viewBox="0 0 26 26"><path d="M15 8 L10 13 L15 18" fill="none" stroke="#555" stroke-width="1.6"/></svg>
    <svg class="abs round-btn" style="top:1908px;left:1071px" viewBox="0 0 26 26"><path d="M11 8 L16 13 L11 18" fill="none" stroke="#555" stroke-width="1.6"/></svg>
  </section>

  <footer>
    <svg class="abs site-footer" width="1200" height="453" viewBox="0 0 1200 453"><path d="M0 63 Q600 -60 1200 63 L1200 453 L0 453 Z" fill="#1c1c1c"/></svg>
    <div class="abs footer-brand"><div class="brand"><span class="brand-mark" style="width:62px;height:62px"></span><span class="brand-name" style="font-size:32px">Claim Vouchly</span></div></div>
    <nav class="abs footer-nav">
      <a>Home</a><span class="sep">|</span><a>Contact Us</a><span class="sep">|</span><a>Testimonials</a><span class="sep">|</span><a>Terms &amp; Conditions</a><span class="sep">|</span><a>Privacy Policy</a>
    </nav>
    <div class="abs social" style="left:457px" aria-label="Social link"></div>
    <div class="abs social" style="left:517px" aria-label="Social link"></div>
    <div class="abs social" style="left:577px" aria-label="Social link"></div>
    <div class="abs social" style="left:638px" aria-label="Social link"></div>
    <div class="abs social" style="left:698px" aria-label="Social link"></div>
    <div class="abs footer-rule"></div>
    <div class="abs copyright">© Copyright 2017 Claim Vouchly. All Rights Reserved</div>
  </footer>

</div>
</body>
</html>
```